Visitenkarten-Design für Stillberaterin
Zielgruppe
Ich bin Stillberaterin ZMRPT, d. h. ich berate Mütter bei Stillschwierigkeiten. Meine Zielgruppe sind junge Familien, die sich vorab über das Stillen Ihres Kindes informieren möchten, Stillschwierigkeiten (z. B. Schmerzen, schlechte Gewichtszunahme usw.) haben oder Fragen rund ums Stillen haben (Medikamente, Stillen in besonderen Situationen...). Weiterhin biete ich Kurse für den Beikoststart oder zum Abstillen an.
Aufgabenstellung
Auf meiner Visitenkarte sollte mein Logo sowie alle Kontaktdaten klar und deutlich erkennbar sein. Die Farben sind dem Logo anzupassen. Die Schriftarten, die im Logo verwendet werden sind: Be Bright und Apple Tree

```html
<!DOCTYPE html>
<html lang="de">
<head>
<meta charset="utf-8">
<title>Visitenkarte – Stillen-in-Ruhe</title>
<link rel="stylesheet" href="https://fonts.googleapis.com/css2?family=Dancing+Script:wght@400;500&family=Nunito:wght@400;500&display=swap">
<style>
  :root {
    --card-bg: #ffffff;
    --card-border: #4a4a4a;
    --brand-pink: #e8649e;
    --name-grey: #7a7474;
    --text-dark: #1e1e1e;
  }
  html, body {
    margin: 0;
    padding: 0;
    width: 1200px;
    height: 777px;
    overflow: hidden;
    background: var(--card-bg);
  }
  .business-card {
    position: relative;
    box-sizing: border-box;
    width: 1200px;
    height: 777px;
    border: 1px solid var(--card-border);
    background: var(--card-bg);
    font-family: "Nunito", sans-serif;
    color: var(--text-dark);
  }
  .brand {
    position: absolute;
    left: 40px;
    top: 340px;
    width: 560px;
    display: flex;
    align-items: center;
    justify-content: center;
    gap: 18px;
  }
  .brand-dot {
    width: 34px;
    height: 34px;
    border-radius: 50%;
    background: var(--brand-pink);
    flex: none;
  }
  .brand-name {
    font-family: "Nunito", sans-serif;
    font-weight: 400;
    font-size: 54px;
    color: var(--brand-pink);
    letter-spacing: 0.5px;
  }
  .person-name {
    position: absolute;
    left: 700px;
    top: 52px;
    margin: 0;
    font-family: "Dancing Script", cursive;
    font-weight: 400;
    font-size: 72px;
    color: var(--name-grey);
  }
  .person-titles {
    position: absolute;
    left: 702px;
    top: 172px;
    margin: 0;
    font-size: 24px;
    line-height: 48px;
  }
  .website {
    position: absolute;
    left: 706px;
    top: 388px;
    margin: 0;
    font-family: "Dancing Script", cursive;
    font-size: 44px;
    color: var(--brand-pink);
  }
  .contact {
    position: absolute;
    left: 709px;
    top: 545px;
    margin: 0;
    font-style: normal;
    font-size: 25px;
    line-height: 39px;
  }
  .contact-gap { display: block; height: 36px; }
</style>
</head>
<body>
  <main class="business-card">
    <div class="brand">
      <span class="brand-dot"></span>
      <span class="brand-name">Stillen-in-Ruhe</span>
    </div>

    <h1 class="person-name">Lena Morwald</h1>
    <p class="person-titles">
      Fachkinderkrankenschwester,<br>
      Still- &amp; Laktationsberaterin ZMRPT
    </p>

    <p class="website">www.stillen-in-ruhe.de</p>

    <address class="contact">
      Am Lindenhang 4<br>
      93049 Musterau
      <span class="contact-gap"></span>
      Telefon: 09401 7710248<br>
      E-Mail: lena@stillen-in-ruhe.de
    </address>
  </main>
</body>
</html>
```